New Template design for Website in Wordpress

We are interested in changing our website look at www.cargolinx.com -We also are very interested in Have it done in Wordpress in which we are understanding the search engines are liking a bit more. The website we would want to try working with on this is www.cargolinx.com. We look forward to seeing the different design ideas please just make sure they are in wordpress! Thanks, Marlen

Reason: need more design idea..... We would still like to use our pictures off our site since we paid for them so keep that in mind as well as we would still want the rotating pictures in the head of the page but not in Flash.

```html
<!DOCTYPE html>
<html lang="en">
<head>
<meta charset="utf-8">
<title>CargoLinx – Freight &amp; Shipping</title>
<link href="https://fonts.googleapis.com/css2?family=Open+Sans:wght@400;600;700;800&display=swap" rel="stylesheet">
<style>
:root{
  --red:#b8271a;
  --red-dark:#9c1f14;
  --red-text:#a8281c;
  --ink:#2e2e2e;
  --muted:#8a8a8a;
  --band:#f6f6f6;
  --dark:#262626;
  --white:#ffffff;
}
*{margin:0;padding:0;box-sizing:border-box}
html,body{width:876px;height:1200px;overflow:hidden;background:var(--white);font-family:"Open Sans",Arial,sans-serif;color:var(--ink)}
.page{position:relative;width:876px;height:1200px}
.abs{position:absolute}
.site-header{left:0;top:0;width:876px;height:68px;background:linear-gradient(#3a3a3a,#1d1d1d)}
.brand{left:116px;top:22px;color:var(--white)}
.brand-name{font-weight:800;font-size:18px;letter-spacing:.5px;line-height:1}
.brand-tag{font-size:10px;margin-top:2px}
.call{right:110px;top:24px;text-align:right;color:var(--white)}
.call small{display:block;font-size:10px;color:#bbb}
.call strong{font-weight:400;font-size:16px}
.main-nav{left:0;top:68px;width:876px;height:34px;background:linear-gradient(#c8321f,#a82113);display:flex;padding-left:118px}
.main-nav a{color:var(--white);text-decoration:none;font-size:12px;font-weight:600;line-height:34px;padding:0 18px;border-right:1px solid rgba(0,0,0,.25)}
.main-nav a:last-child{border-right:none}
.hero{left:0;top:102px;width:876px;height:369px;background:linear-gradient(180deg,#b9cde0 0%,#dfe6ea 30%,#7f8c8c 45%,#8a8883 65%,#6e6c68 100%)}
.hero-caption{left:109px;top:223px;width:310px;height:120px;background:rgba(60,60,60,.82);padding:20px 0 0 21px;color:var(--white)}
.hero-caption h1{font-weight:400;font-size:19px;letter-spacing:.3px}
.hero-caption p{font-size:8px;line-height:13px;margin-top:5px}
.btn{display:inline-block;background:var(--red);color:var(--white);font-weight:600;text-decoration:none;text-align:center}
.hero-caption .btn{margin-top:7px;width:109px;height:26px;line-height:26px;font-size:11px}
.dots{left:421px;top:450px;display:flex;gap:4px}
.dots span{width:9px;height:9px;border-radius:50%;background:var(--white)}
.intro{left:0;top:498px;width:876px;text-align:center}
.intro h2{font-weight:600;font-size:20px;letter-spacing:.3px}
.intro h3{font-weight:400;font-size:13px;margin-top:8px}
.intro p{font-size:8px;line-height:14.5px;color:var(--muted);width:610px;margin:6px auto 0}
.rule{left:106px;top:624px;width:665px;height:1px;background:#e2e2e2}
.band{left:9px;top:624px;width:867px;height:206px;background:var(--band)}
.card{top:654px;width:158px;height:150px;background:var(--white);box-shadow:0 0 2px rgba(0,0,0,.1)}
.card .photo{width:158px;height:86px}
.card h4{color:var(--red-text);font-weight:600;font-size:11px;line-height:13px;margin:10px 12px 0;text-transform:uppercase}
.card p{font-size:7.5px;line-height:13px;color:#666;margin:3px 12px 0}
.what{left:0;top:853px;width:876px;text-align:center;font-weight:400;font-size:18px}
.service{top:898px;width:160px;text-align:center}
.service .icon{width:66px;height:66px;border-radius:50%;border:1px solid #e6e6e6;margin:0 auto;display:flex;align-items:center;justify-content:center;box-shadow:0 1px 2px rgba(0,0,0,.06)}
.service h5{font-weight:400;font-size:11.5px;line-height:18px;margin-top:12px}
.service p{font-size:7.5px;line-height:13px;color:var(--muted);margin-top:4px}
.service .btn{width:78px;height:22px;line-height:22px;font-size:9.5px;margin-top:8px;background:var(--red-dark)}
.site-footer{left:0;top:1116px;width:876px;height:84px;background:var(--dark)}
.foot-nav{left:113px;top:1139px;color:var(--white);font-size:10.5px}
.foot-nav a{color:var(--white);text-decoration:none}
.foot-nav i{font-style:normal;margin:0 5px;color:var(--white)}
.copy{left:113px;top:1161px;font-size:8.5px;color:#aaa}
.social{left:688px;top:1138px;display:flex;gap:3px}
.social span{width:17px;height:17px;border-radius:50%;background:var(--white)}
</style>
</head>
<body>
<div class="page">
  <header class="site-header abs"></header>
  <div class="brand abs">
    <div class="brand-name">CARGOLINX</div>
    <div class="brand-tag">A FULL-SERVICE FREIGHT COMPANY</div>
  </div>
  <div class="call abs"><small>Call Us Now</small><strong>555.014.2290</strong></div>
  <nav class="main-nav abs">
    <a href="#">HOME</a><a href="#">INSURANCE &amp; LEGAL INFO</a><a href="#">ABOUT US</a><a href="#">FAST FRIEGHT QUOTE</a><a href="#">CONTACT</a>
  </nav>

  <div class="hero abs" role="img" aria-label="Red shipping container truck driving along a coastal mountain road"></div>
  <div class="hero-caption abs">
    <h1>FREIGHT &amp; SHIPPING SERVICE</h1>
    <p>Lorem ipsum dolor sit amet consectetuer adipiscing elit Nam cursus<br>Morbi ut mi Nullam enim leo egestas</p>
    <a class="btn" href="#">GET A QUOTE</a>
  </div>
  <div class="dots abs"><span></span><span></span><span></span><span></span></div>

  <section class="intro abs">
    <h2>GET FAST &amp; FREE FREIGHT QUOTES NOW AND SAVE!!</h2>
    <h3>WORLDWIDE SHIPPING- OCEAN AND TRUCKING WITH NO LIMITS</h3>
    <p>Welcome to CargoLinx and Meridian Haul Inc. We are a one stop solution logistics company servicing Worldwide with our Trucking and Ocean shipping service. In using our freight services, we will negotiate a competitive freight quote using over 5000 different carriers who are certified and contracted by us. We have all equipment types available daily, service all freight types, and have no limits Worldwide.</p>
  </section>

  <div class="band abs"></div>
  <div class="rule abs"></div>

  <article class="card abs" style="left:110px">
    <div class="photo" role="img" aria-label="Red heavy haul truck on highway" style="background:linear-gradient(#9fb9d4,#c9614a 60%,#5a5550)"></div>
    <h4>Heavy Haul Services</h4>
    <p>Dui Nulla elementum dui ut augue Aliquam vehicula mi at mauris</p>
  </article>
  <article class="card abs" style="left:277px">
    <div class="photo" role="img" aria-label="Refrigerated trailer truck on road" style="background:linear-gradient(#c9d8c2,#e8e8e8 45%,#7d8a7a)"></div>
    <h4>Dry &amp; Refrigerated</h4>
    <p>Dui Nulla elementum dui ut augue Aliquam vehicula mi at mauris</p>
  </article>
  <article class="card abs" style="left:445px">
    <div class="photo" role="img" aria-label="Blue truck at a loading dock" style="background:linear-gradient(#dcdcdc,#b7bcc6 50%,#3a4a7a)"></div>
    <h4>Flated, Step Deck &amp;<br>Piggy Back</h4>
    <p>Nulla elementum dui ut augue Aliqua</p>
  </article>
  <article class="card abs" style="left:612px">
    <div class="photo" role="img" aria-label="Cargo ship at sea" style="background:linear-gradient(#8fb3d6,#5f8fb3 55%,#2f5f78)"></div>
    <h4>Frieght<br>Forwarding Ocean</h4>
    <p>Dui ut augue Aliquam vehicula mi at</p>
  </article>

  <h2 class="what abs">WHAT WE DO</h2>

  <div class="service abs" style="left:112px">
    <div class="icon"><svg width="36" height="30" viewBox="0 0 36 30"><rect x="8" y="2" width="8" height="7" fill="#b8271a"/><rect x="4" y="9" width="16" height="6" fill="#b8271a"/><path d="M1 15h34l-5 12H5z" fill="#b8271a"/></svg></div>
    <h5>WORLDWIDE<br>FREIGHT SERVICES</h5>
    <p>Ut nisi erat fermentum vel congue id euis-<br>mod in elit Fusce ultricies orci ac</p>
    <a class="btn" href="#">READ MORE</a>
  </div>
  <div class="service abs" style="left:279px">
    <div class="icon"><svg width="30" height="32" viewBox="0 0 30 32"><rect x="2" y="2" width="26" height="14" fill="#b8271a"/><rect x="4" y="17" width="22" height="10" rx="2" fill="#b8271a"/><rect x="8" y="19" width="14" height="4" fill="#fff"/><rect x="5" y="27" width="5" height="4" fill="#b8271a"/><rect x="20" y="27" width="5" height="4" fill="#b8271a"/></svg></div>
    <h5>FREIGHT<br>TRUCKING SERVICE</h5>
    <p>Ut nisi erat fermentum vel congue id euis-<br>mod in elit Fusce ultricies orci ac</p>
    <a class="btn" href="#">READ MORE</a>
  </div>
  <div class="service abs" style="left:439px">
    <div class="icon"><svg width="30" height="36" viewBox="0 0 30 36"><rect x="14" y="1" width="2" height="6" fill="#b8271a"/><rect x="9" y="7" width="12" height="5" fill="#b8271a"/><path d="M4 12h22l-3 14-8 3-8-3z" fill="#b8271a"/><path d="M3 32q3-3 6 0t6 0 6 0 6 0" stroke="#b8271a" stroke-width="2" fill="none"/></svg></div>
    <h5>OCEAN SHIPPING<br>SERVICES</h5>
    <p>Ut nisi erat fermentum vel congue id euis-<br>mod in elit Fusce ultricies orci ac</p>
    <a class="btn" href="#">READ MORE</a>
  </div>
  <div class="service abs" style="left:603px">
    <div class="icon"><svg width="34" height="34" viewBox="0 0 34 34"><path d="M17 2 31 9 17 16 3 9z" fill="#b8271a"/><path d="M3 11l13 7v14L3 25z" fill="#b8271a"/><path d="M31 11l-13 7v14l13-7z" fill="#9c1f14"/></svg></div>
    <h5>WE SHIP IT ALL<br>WORLDWIDE!</h5>
    <p>Ut nisi erat fermentum vel congue id euis-<br>mod in elit Fusce ultricies orci ac</p>
    <a class="btn" href="#">READ MORE</a>
  </div>

  <footer class="site-footer abs"></footer>
  <div class="foot-nav abs"><a href="#">HOME</a><i>|</i><a href="#">INSURANCE &amp; LEGAL INFO</a><i>|</i><a href="#">ABOUT US</a><i>|</i><a href="#">FAST FRIEGHT QUOTE</a><i>|</i><a href="#">CONTACT</a></div>
  <div class="copy abs">© 2014 Company Name &nbsp;All right reserved &nbsp;Term of Use</div>
  <div class="social abs"><span></span><span></span><span></span><span></span></div>
</div>
</body>
</html>
```